Vodka label designing in name of brand name KESTRAVO

We need a label design for VODKA.Name of brand is KESTRAVO.
Targeted consumers are are young males and females.
Product will be in different 7 flavours.
Product will be triple distilled and silver filtered very rich and premium quality product.
I have to keep same theme for different flavours of vodka.
only colour and image of fruit will change.
As the name suggest its KESTRAVO its liberty to drink and be happy.
Label Design must be very rich,simple,attractive and unforgettable just like inside product.

Target Market(s)

YOUTH males and females, bar tenders,mixers, universal product

Industry/Entity Type

Product

Requirements
Must have
• rich look and easy to remember.
Nice to have
• any connection with WORD KESTRAVO
Should not have
• ANYTHING RELATED TO KESTRAVO FIGNTING

```html
<!DOCTYPE html>
<html lang="en">
<head>
<meta charset="utf-8">
<title>KESTRAVO Vodka – Flavour Labels</title>
<link rel="stylesheet" href="https://fonts.googleapis.com/css2?family=Josefin+Sans:wght@300;600&family=Great+Vibes&display=swap">
<style>
  :root {
    --canvas-bg: #eef2f5;
    --label-top: #cfe0ea;
    --label-mid: #eef5f9;
    --label-edge: #9fc0d3;
    --raspberry: #b0104f;
    --raspberry-soft: #e0406f;
    --lime-brand: #1f5cc8;
    --lime-script: #6f8a1e;
    --lime-green: #8cc63f;
    --lemon-yellow: #f5d44a;
    --peach: #c2621c;
    --peach-script: #b5541a;
    --peach-flesh: #f6b04a;
    --peach-skin: #e0502a;
    --leaf: #6aa33a;
  }
  html, body {
    margin: 0;
    padding: 0;
    overflow: hidden;
  }
  .canvas {
    position: relative;
    width: 1108px;
    height: 1200px;
    background: var(--canvas-bg);
    overflow: hidden;
  }
  .label {
    position: absolute;
    top: 200px;
    width: 320px;
    height: 800px;
    border-radius: 24px;
    background: linear-gradient(90deg, var(--label-edge) 0%, var(--label-mid) 35%, var(--label-mid) 60%, var(--label-top) 100%);
    display: flex;
    flex-direction: column;
    align-items: center;
  }
  .label--raspberry { left: 42px; --brand: var(--raspberry); --script: var(--raspberry); }
  .label--lime { left: 394px; --brand: var(--lime-brand); --script: var(--lime-script); }
  .label--peach { left: 746px; --brand: var(--peach); --script: var(--peach-script); }

  .brand-dot {
    margin-top: 120px;
    width: 44px;
    height: 44px;
    border-radius: 50%;
    background: var(--brand);
  }
  .brand-name {
    margin-top: 22px;
    font-family: "Josefin Sans", sans-serif;
    font-weight: 300;
    font-size: 46px;
    letter-spacing: 1px;
    color: var(--brand);
    line-height: 1;
  }
  .brand-type {
    margin-top: 12px;
    font-family: "Josefin Sans", sans-serif;
    font-weight: 600;
    font-size: 14px;
    letter-spacing: 10px;
    padding-left: 10px;
    color: var(--brand);
  }
  .flavour-name {
    margin-top: 130px;
    font-family: "Great Vibes", cursive;
    font-size: 56px;
    color: var(--script);
    line-height: 1;
  }
  .fruit-art {
    margin-top: 24px;
    width: 200px;
    height: 130px;
    border-radius: 50%;
  }
  .fruit-art--raspberry { background: radial-gradient(circle at 45% 55%, var(--raspberry-soft), var(--raspberry) 60%, var(--leaf) 100%); }
  .fruit-art--lime { background: linear-gradient(90deg, var(--lime-green) 0%, var(--lime-green) 40%, var(--lemon-yellow) 60%, var(--lemon-yellow) 100%); }
  .fruit-art--peach { background: radial-gradient(circle at 40% 55%, var(--peach-flesh), var(--peach-skin) 70%, var(--leaf) 100%); }
</style>
</head>
<body>
<main class="canvas">
  <section class="label label--raspberry">
    <div class="brand-dot"></div>
    <div class="brand-name">KESTRAVO</div>
    <div class="brand-type">VODKA</div>
    <div class="flavour-name">Raspberry</div>
    <div class="fruit-art fruit-art--raspberry" role="img" aria-label="Raspberries with green leaves"></div>
  </section>

  <section class="label label--lime">
    <div class="brand-dot"></div>
    <div class="brand-name">KESTRAVO</div>
    <div class="brand-type">VODKA</div>
    <div class="flavour-name">Lime</div>
    <div class="fruit-art fruit-art--lime" role="img" aria-label="Halved lime and lemon"></div>
  </section>

  <section class="label label--peach">
    <div class="brand-dot"></div>
    <div class="brand-name">KESTRAVO</div>
    <div class="brand-type">VODKA</div>
    <div class="flavour-name">Peach</div>
    <div class="fruit-art fruit-art--peach" role="img" aria-label="Whole and halved peach with a leaf"></div>
  </section>
</main>
</body>
</html>
```